indépendant en tant que Massothérapeute et Préparateur Mental, j'ai besoin de ...

Massothérapeute et préparateur mental indépendant, je recherche une carte de visite sobre et dynamique, sans images liées au massage ou à la préparation mentale mais intégrant mon logo. Les couleurs que j'aime bien sont : Blanc, gris, anthracite, noir et jaune

carte de préférence Horizontale
neutre qui puisse toucher le deux domaines Massothérapie et préparation mentale

Requirements
Must have
• mon projet doit intégrer au recto:
LOGO
Loïc Bardemaz
078 315 26 48
info@loicbardemaz-exemple.ch
et éventuellement www.loicbardemaz-exemple.ch

et au verso les deux adresses:

Chemin des Grèvelins 7B
1400 Yverdon-les-Bains

Avenue des Mélèzes 9
1700 Fribourg

Should not have
• mon projet ne doit pas contenir d'image en liens avec le massage ni la préparation mentale.

```html
<!DOCTYPE html>
<html lang="fr">
<head>
<meta charset="UTF-8">
<title>Loïc Bardemaz – Cartes de visite</title>
<link rel="stylesheet" href="https://fonts.googleapis.com/css2?family=Lato:wght@400;700&display=swap">
<style>
  :root {
    --backdrop: #e4e4e4;
    --anthracite: #2c2c2c;
    --band-dark: #050505;
    --band-light: #1f1f1f;
    --white: #ffffff;
    --ink: #1a1a1a;
    --divider: #cfcfcf;
    --bar-black: #0b0b0b;
    --bar-grey: #3a3a3a;
  }
  * { margin: 0; padding: 0; box-sizing: border-box; }
  html, body {
    width: 1200px; height: 801px; overflow: hidden;
    background: var(--backdrop);
    font-family: "Lato", sans-serif;
  }
  .canvas { position: relative; width: 1200px; height: 801px; }

  .card {
    position: absolute; left: 354px; width: 516px; height: 309px;
    overflow: hidden;
  }

  /* Verso */
  .card-back { top: 44px; background: var(--anthracite); }
  .address-band {
    position: absolute; left: 0; top: 104px; width: 100%; height: 102px;
    background: radial-gradient(ellipse at 50% 30%, var(--band-light) 0%, var(--band-dark) 70%);
  }
  .band-name {
    position: absolute; top: 18px; left: 0; width: 100%;
    text-align: center; color: var(--white);
    font-weight: 700; font-size: 15px; letter-spacing: 0.5px;
  }
  .address {
    position: absolute; top: 56px;
    color: var(--white); font-size: 11px; line-height: 15px; letter-spacing: 0.2px;
  }
  .address-primary { left: 75px; }
  .address-secondary { left: 290px; }
  .pin { position: absolute; left: 50px; top: 58px; width: 16px; height: 22px; }

  /* Recto */
  .card-front { top: 424px; background: var(--white); }
  .brand {
    position: absolute; left: 37px; top: 144px;
    display: flex; align-items: center; gap: 8px;
    color: var(--ink); font-weight: 700; font-size: 19px;
  }
  .brand-square { width: 14px; height: 14px; background: var(--ink); }
  .divider {
    position: absolute; left: 259px; top: 100px; width: 1px; height: 118px;
    background: var(--divider);
  }
  .contact-name {
    position: absolute; left: 288px; top: 104px;
    font-size: 18px; font-weight: 700; color: var(--ink); letter-spacing: 0.3px;
  }
  .contact-list {
    position: absolute; left: 290px; top: 145px; list-style: none;
    font-size: 13px; line-height: 21.5px; color: var(--ink); letter-spacing: 0.3px;
  }
  .contact-list b { display: inline-block; width: 16px; font-weight: 700; }
  .bottom-bar {
    position: absolute; left: 0; bottom: 0; width: 100%; height: 8px;
    display: flex; gap: 2px;
  }
  .bar-main { width: 406px; background: var(--bar-black); }
  .bar-end { flex: 1; background: var(--bar-grey); }
</style>
</head>
<body>
<div class="canvas">

  <section class="card card-back">
    <div class="address-band">
      <div class="band-name">Loïc Bardemaz</div>
      <svg class="pin" viewBox="0 0 16 22" aria-hidden="true">
        <path d="M8 0C3.6 0 0 3.5 0 7.9 0 13.5 8 22 8 22s8-8.5 8-14.1C16 3.5 12.4 0 8 0z" fill="#ffffff"/>
        <circle cx="8" cy="7.8" r="3" fill="#050505"/>
      </svg>
      <p class="address address-primary">Chemin des Grèvelins 7B<br>1400 Yverdon-les-Bains</p>
      <p class="address address-secondary">Avenue des Mélèzes 9<br>1700 Fribourg</p>
    </div>
  </section>

  <section class="card card-front">
    <div class="brand"><span class="brand-square"></span>Loïc Bardemaz</div>
    <div class="divider"></div>
    <h1 class="contact-name">Loïc Bardemaz</h1>
    <ul class="contact-list">
      <li><b>M</b>: 078 315 26 48</li>
      <li><b>E</b>: info@loicbardemaz-exemple.ch</li>
      <li><b>W</b>: www.loicbardemaz-exemple.ch</li>
    </ul>
    <div class="bottom-bar">
      <span class="bar-main"></span>
      <span class="bar-end"></span>
    </div>
  </section>

</div>
</body>
</html>
```